K & D A/C Compressors' Business Card

Hello,

I need someone to create a new business card for my business. The name of my Business is: K & D A/C Compressors. I sell automotive air conditioning parts (a/c parts). I would like the business card to incorporate my logo, and to have an automotive feel to it. It is important that the business card feel like it is coming from an automotive parts business.

I already have a logo, which I will provide.

Thanks.
Updates

Project Deadline Extended Reason: I feel like extending the deadline until October 9, 2017, will allow for more time to design the business card. Thank you for your understanding. Added Monday, October 2, 2017

Target Market(s)

Consumers who need automotive a/c parts, and auto mechanics.

Industry/Entity Type

Automotive

Contact Information for Business Card

Business name: K & D A/C Compressors
Business Address: 48207 Southwest 36th Street, North Miami Beach, Florida 33162
Telephone: 305-472-1390
Fax: To be provided once I choose your design.
Website: www.kdcoolunits.example
Email: support@kdcoolunits.example
Names: To be provided once I choose your design.

Font styles to use
Sans Serif

Colors

Designer to choose colors to be used in the design.

Requirements
Must have
• The business card must include all of the "Business Card Details" and the logo I have uploaded.

```html
<!DOCTYPE html>
<html lang="en">
<head>
<meta charset="UTF-8">
<title>K &amp; D A/C Compressors – Business Card</title>
<link rel="stylesheet" href="https://fonts.googleapis.com/css2?family=Open+Sans:wght@400;600&display=swap">
<style>
  :root {
    --stage: #3a3a3c;
    --card-dark: #000000;
    --card-light: #ffffff;
    --brand-blue: #1fa3e0;
    --brand-grey: #a7a9ac;
    --text-grey: #555759;
    --band-grey: #b5b6b8;
  }
  * { margin: 0; padding: 0; box-sizing: border-box; }
  html, body {
    width: 1200px; height: 864px; overflow: hidden;
    background: var(--stage);
    font-family: "Open Sans", Arial, sans-serif;
  }
  .canvas { position: relative; width: 1200px; height: 864px; }

  .card {
    position: absolute; width: 560px; height: 320px;
    overflow: hidden;
    box-shadow: 0 10px 30px rgba(0,0,0,.45);
  }
  .card--front { left: 120px; top: 80px; background: var(--card-dark); }
  .card--back  { left: 520px; top: 464px; background: var(--card-light); }

  .brand {
    position: absolute; display: flex; align-items: center; gap: 12px;
    color: var(--brand-grey); font-weight: 600; white-space: nowrap;
  }
  .brand__mark { display: block; background: var(--brand-blue); }
  .card--front .brand { left: 50%; top: 50%; transform: translate(-50%, -50%); font-size: 30px; }
  .card--front .brand__mark { width: 22px; height: 22px; }
  .card--back .brand { right: 34px; top: 34px; font-size: 22px; }
  .card--back .brand__mark { width: 16px; height: 16px; }

  .holder { position: absolute; left: 34px; top: 150px; }
  .holder__name { color: var(--brand-blue); font-weight: 600; font-size: 24px; line-height: 1.1; }
  .holder__title { color: var(--text-grey); font-size: 16px; }

  .divider { position: absolute; left: 34px; right: 34px; top: 210px; height: 1.5px; background: var(--brand-blue); }

  .contacts { position: absolute; left: 34px; top: 218px; list-style: none; }
  .contacts li { display: flex; align-items: center; gap: 8px; color: var(--text-grey); font-size: 15px; line-height: 20px; }
  .contacts svg { width: 14px; height: 14px; fill: var(--brand-blue); flex: none; }

  .address {
    position: absolute; right: 34px; top: 218px; text-align: right;
    color: var(--text-grey); font-size: 15px; line-height: 20px;
  }

  .band-grey { position: absolute; left: 0; bottom: 0; width: 100%; height: 6px; background: var(--band-grey); }
  .band-blue {
    position: absolute; right: 0; bottom: 0; width: 290px; height: 34px;
    background: var(--brand-blue);
    clip-path: polygon(22px 0, 100% 0, 100% 100%, 0 100%);
    display: flex; align-items: center; justify-content: flex-end; padding-right: 24px;
  }
  .band-blue__url { color: #ffffff; font-size: 15px; font-weight: 600; }
</style>
</head>
<body>
<main class="canvas">
  <section class="card card--front" aria-label="Card front">
    <div class="brand"><span class="brand__mark"></span><span>K &amp; D A/C Compressors</span></div>
  </section>

  <section class="card card--back" aria-label="Card back">
    <div class="brand"><span class="brand__mark"></span><span>K &amp; D A/C Compressors</span></div>

    <div class="holder">
      <p class="holder__name">Marco Alvarez</p>
      <p class="holder__title">President</p>
    </div>

    <div class="divider"></div>

    <ul class="contacts">
      <li>
        <svg viewBox="0 0 16 16" aria-hidden="true"><path d="M3.6 1.5l2.3 2.3-1.3 2a9 9 0 0 0 5.6 5.6l2-1.3 2.3 2.3-1.6 2C7.6 15.6.4 8.4 1.6 3.1z"/></svg>
        <span>305-472-1390</span>
      </li>
      <li>
        <svg viewBox="0 0 16 16" aria-hidden="true"><path d="M4 1h8v4H4z M1 6h14v7h-3v2H4v-2H1z M5 10v4h6v-4z"/></svg>
        <span>01 012-555-0142</span>
      </li>
      <li>
        <svg viewBox="0 0 16 16" aria-hidden="true"><path d="M1 3h14v10H1z M2 4l6 5 6-5v-.2H2z" fill-rule="evenodd"/></svg>
        <span>support@kdcoolunits.example</span>
      </li>
    </ul>

    <p class="address">48207 Southwest 36th Street,<br>Coral Vista, Florida 33099</p>

    <div class="band-grey"></div>
    <div class="band-blue"><span class="band-blue__url">www.kdcoolunits.example</span></div>
  </section>
</main>
</body>
</html>
```